Plum Meadow Label

Design a label for new brand called Plum Meadow. The specific product label :
Plum Meadow Cocoa Butter Lotion. You only need to design the front label.
I have included the logo and a bottle jpeg with 2 bottles on it. Please try your best.

Industry/Entity Type

Product

Requirements
Must have
• text on the label other than the logo:
cocoa butter
lotion
8.5oz/250ml

Original Moisturizing Formula
Smoothes Marks
Protect Skin

__________________________________
- ALTERNATIVE TEXT TO ALSO USE:
Smoothes Dry Skin, Blemishes & Stretch Marks
Softens Hands, Face and Body
Vitamin E

```html
<!DOCTYPE html>
<html lang="en">
<head>
<meta charset="utf-8">
<title>Plum Meadow Cocoa Butter Lotion – Front Label</title>
<link href="https://fonts.googleapis.com/css2?family=Arimo:wght@400;700&family=Roboto+Condensed:wght@400;700&display=swap" rel="stylesheet">
<style>
  :root{
    --page:#e4d1a4;
    --olive-dark:#46552f;
    --olive-deep:#3b4927;
    --olive-mid:#8e9760;
    --cream:#f4eecf;
    --cream-soft:#efe8d2;
    --gold:#c9a85a;
    --gold-light:#efdc9d;
    --ink:#3a4526;
    --ink-soft:#4d4a3c;
  }
  html,body{margin:0;padding:0;width:961px;height:1200px;overflow:hidden;background:var(--page);}
  .canvas{position:relative;width:961px;height:1200px;}
  .label{
    position:absolute;left:200px;top:40px;width:560px;height:1120px;
    border-radius:44px 44px 30px 30px;overflow:hidden;
    background:linear-gradient(180deg,var(--olive-mid) 0%,var(--olive-mid) 42%,#b7b88f 62%,var(--cream-soft) 78%,var(--cream-soft) 100%);
    box-shadow:0 6px 18px rgba(80,60,20,.18);
    font-family:"Arimo",Arial,sans-serif;
  }
  .brand-band{
    position:absolute;left:0;top:0;width:560px;height:235px;
    background:linear-gradient(180deg,var(--olive-deep),var(--olive-dark));
    display:flex;align-items:center;justify-content:center;
  }
  .brand-name{
    font-family:"Roboto Condensed",Arial,sans-serif;font-weight:400;
    font-size:62px;color:var(--cream);letter-spacing:1px;margin-top:70px;
  }
  .gold-rule{position:absolute;left:0;width:560px;height:6px;
    background:linear-gradient(90deg,var(--gold),var(--gold-light),var(--gold));}
  .gold-rule.top{top:235px;}
  .title-band{
    position:absolute;left:0;top:241px;width:560px;height:180px;
    background:linear-gradient(180deg,#fbf6dc,var(--cream));
    text-align:center;
  }
  .product-title{
    margin:32px 0 0;font-family:"Roboto Condensed",Arial,sans-serif;font-weight:700;
    font-size:66px;line-height:68px;color:var(--ink);letter-spacing:.5px;
  }
  .formula-band{position:absolute;left:0;top:421px;width:560px;height:112px;}
  .formula-band svg{position:absolute;left:0;top:0;}
  .formula-text{
    position:absolute;left:0;top:22px;width:560px;text-align:center;
    color:var(--cream);font-size:24px;line-height:30px;letter-spacing:4px;
  }
  .portrait{
    position:absolute;left:213px;top:560px;width:134px;height:134px;border-radius:50%;
    background:radial-gradient(circle at 50% 45%,#f3ddd0,#d9b8a4);
    box-shadow:0 0 0 5px #e9dfc4,0 0 0 7px #b9ae86;
  }
  .claims{
    position:absolute;left:0;top:698px;width:560px;text-align:center;
    font-weight:700;font-size:22px;line-height:31px;color:#2c2c22;
  }
  .cocoa-art{
    position:absolute;left:30px;top:770px;width:290px;height:210px;border-radius:40% 50% 45% 40%;
    background:radial-gradient(ellipse at 60% 55%,#8a5430 0%,#a0683c 30%,#7fa057 60%,rgba(239,232,210,0) 78%);
  }
  .benefits{
    position:absolute;left:34px;top:980px;margin:0;padding:0;list-style:none;
    font-size:16px;line-height:27px;color:var(--ink-soft);
  }
  .net-content{
    position:absolute;right:40px;top:1038px;font-size:18px;color:var(--ink-soft);
  }
</style>
</head>
<body>
<div class="canvas">
  <div class="label">
    <header class="brand-band">
      <div class="brand-name">Plum Meadow</div>
    </header>
    <div class="gold-rule top"></div>
    <section class="title-band">
      <h1 class="product-title">COCOA BUTTER<br>LOTION</h1>
    </section>
    <section class="formula-band">
      <svg width="560" height="112" viewBox="0 0 560 112" aria-hidden="true">
        <defs>
          <linearGradient id="bandGold" x1="0" x2="1">
            <stop offset="0" stop-color="#c9a85a"/><stop offset=".5" stop-color="#efdc9d"/><stop offset="1" stop-color="#c9a85a"/>
          </linearGradient>
        </defs>
        <path d="M0 0H560V84Q280 112 0 84Z" fill="var(--olive-dark)"/>
        <rect x="0" y="0" width="560" height="4" fill="url(#bandGold)"/>
      </svg>
      <div class="formula-text">ORIGINAL<br>MOISTURIZING FORMULA</div>
    </section>
    <div class="portrait" role="img" aria-label="Round photo of a woman applying lotion to her cheek"></div>
    <div class="claims">Smoothes Marks<br>Protect Skin</div>
    <div class="cocoa-art" role="img" aria-label="Illustration of a cocoa pod cut open with beans and green leaves"></div>
    <ul class="benefits">
      <li>Smoothes Dry Skin</li>
      <li>Blemishes &amp; Stretch Marks</li>
      <li>Softens Hands, Face and Body</li>
      <li>Vitamin E</li>
    </ul>
    <div class="net-content">8.5oz (250 ml)</div>
  </div>
</div>
</body>
</html>
```